Realtor business card

Looking for a business card that will stand out from the rest. My area of expertise is residential real estate and loans.

Industry/Entity Type

Residential

Requirements
Must have
• Owen Blakely, SFR
Broker
Mortgage Loan Originator
Notary Public
DRE License #07392518
NMLS 581637
Cell 714-529-4170
Fax 888-415-2967
www.owenblakely-example.com
ob@owenblakely-example.com

```html
<!DOCTYPE html>
<html lang="en">
<head>
<meta charset="utf-8">
<title>Owen Blakely — Business Card Back</title>
<link rel="stylesheet" href="https://fonts.googleapis.com/css2?family=Myriad+Pro&family=PT+Sans:wght@400&display=swap">
<style>
  :root {
    --card-bg: #3a3a3c;
    --corner: #000000;
    --text: #ffffff;
  }
  html, body {
    margin: 0;
    padding: 0;
    width: 1200px;
    height: 695px;
    overflow: hidden;
    background: var(--card-bg);
  }
  .card-back {
    position: relative;
    width: 1200px;
    height: 695px;
    background: var(--card-bg);
    overflow: hidden;
  }
  .corner-accent {
    position: absolute;
    right: 0;
    bottom: 0;
    width: 1200px;
    height: 695px;
  }
  .contact-block {
    position: absolute;
    left: 0;
    right: 0;
    top: 202px;
    margin: 0;
    text-align: center;
    color: var(--text);
    font-family: "PT Sans", "Myriad Pro", sans-serif;
    font-size: 34px;
    line-height: 46.5px;
    font-weight: 400;
  }
  .contact-line {
    display: block;
  }
</style>
</head>
<body>
  <main class="card-back">
    <svg class="corner-accent" viewBox="0 0 1200 695" aria-hidden="true">
      <polygon points="1200,412 1200,695 950,695" fill="var(--corner)"/>
    </svg>
    <address class="contact-block" style="font-style: normal;">
      <span class="contact-line">DRE License #07392518</span>
      <span class="contact-line">NMLS 581637</span>
      <span class="contact-line">Cell 714-529-4170</span>
      <span class="contact-line">Fax 888-415-2967</span>
      <span class="contact-line">www.owenblakely-example.com</span>
      <span class="contact-line">ob@owenblakely-example.com</span>
    </address>
  </main>
</body>
</html>
```